Bramblewick Keystone

Looking for modern business cards.
Clean contemporary design.
Similar to this.
https://www.snapvorlo.net/imgview?src=https%3A%2F%2Fcdn.printquell.net%2Fprofessional_elegant_modern_black_plain_metal_business_card-a1b2c3d4e5f60718293a4b5c6d7e8f90_qwxyz_4tmpl_540.jpg&ref=https%3A%2F%2Fwww.printquell.net%2Fprofessional_elegant_modern_black_plain_metal_business_card-100200300400500600&id=7aB9cD3e-QR5TU&tid=Xyz_abc123defGH%3A&v=10abcDEFghiJKLmnoPQRstUVwxYZ0123456789abcd..x&w=540&h=540&bih=1360&biw=1061&q=modern%20business%20cards&ref2=0abcDEFghiJKLmnoPQRstUVwxYZ0123456789abcd&ia=mrc&ua=8

But I'd like the blue to look metallic.

```html
<!DOCTYPE html>
<html lang="en">
<head>
<meta charset="utf-8">
<title>Bramblewick Keystone – Business Card</title>
<link href="https://fonts.googleapis.com/css2?family=Noticia+Text:wght@400;700&display=swap" rel="stylesheet">
<style>
  :root {
    --backdrop: #86a5b8;
    --metal-edge: #15283a;
    --metal-mid: #0d5f88;
    --metal-bright: #0b8cc2;
    --card-white: #ffffff;
    --ink: #3a3a3a;
    --accent: #1f9ac4;
    --brand-white: #ffffff;
  }
  * { margin: 0; padding: 0; box-sizing: border-box; }
  html, body {
    width: 1097px;
    height: 1200px;
    overflow: hidden;
    background: var(--backdrop);
    font-family: "Noticia Text", Georgia, serif;
  }
  .canvas {
    position: relative;
    width: 1097px;
    height: 1200px;
  }
  .card {
    position: absolute;
    left: 220px;
    width: 657px;
    height: 401px;
    border-radius: 26px;
    overflow: hidden;
  }
  .card--front {
    top: 141px;
    background:
      repeating-linear-gradient(180deg,
        rgba(255,255,255,0.05) 0px, rgba(255,255,255,0.05) 1px,
        rgba(0,0,0,0.04) 2px, rgba(0,0,0,0) 3px, rgba(255,255,255,0.03) 5px),
      linear-gradient(180deg, rgba(255,255,255,0.10) 0%, rgba(255,255,255,0) 35%, rgba(0,0,0,0.12) 100%),
      linear-gradient(90deg,
        var(--metal-edge) 0%, #173e58 18%, var(--metal-mid) 38%,
        var(--metal-bright) 52%, var(--metal-mid) 66%, #173e58 84%, var(--metal-edge) 100%);
  }
  .front-brand {
    position: absolute;
    left: 0;
    right: 0;
    top: 195px;
    display: flex;
    align-items: center;
    justify-content: center;
    gap: 16px;
  }
  .front-brand__name {
    font-size: 38px;
    font-weight: 700;
    color: var(--brand-white);
    letter-spacing: -0.5px;
  }
  .front-brand__dot {
    width: 16px;
    height: 16px;
    border-radius: 50%;
    background: var(--brand-white);
  }
  .card--back {
    top: 635px;
    background: var(--card-white);
    color: var(--ink);
  }
  .holder-name {
    position: absolute;
    left: 38px;
    top: 46px;
    font-size: 22px;
    line-height: 28px;
  }
  .contact-block {
    position: absolute;
    left: 322px;
    font-size: 19px;
    line-height: 27px;
  }
  .contact-block--address { top: 46px; }
  .contact-block--phones { top: 212px; }
  .contact-line { white-space: nowrap; }
  .contact-icon {
    position: absolute;
    left: 292px;
    width: 20px;
    height: 20px;
  }
  .back-brand {
    position: absolute;
    left: 38px;
    top: 332px;
    display: flex;
    align-items: center;
    gap: 8px;
  }
  .back-brand__name {
    font-size: 20px;
    font-weight: 700;
    color: var(--accent);
    letter-spacing: -0.3px;
  }
  .back-brand__dot {
    width: 9px;
    height: 9px;
    border-radius: 50%;
    background: var(--accent);
  }
</style>
</head>
<body>
<main class="canvas">

  <section class="card card--front" aria-label="Card front">
    <div class="front-brand">
      <span class="front-brand__name">Bramblewick Keystone</span>
      <span class="front-brand__dot"></span>
    </div>
  </section>

  <section class="card card--back" aria-label="Card back">
    <p class="holder-name">Edwin Halloway</p>

    <svg class="contact-icon" style="top:50px" viewBox="0 0 24 24" aria-hidden="true">
      <path fill="var(--accent)" d="M12 2a7 7 0 0 0-7 7c0 5 7 13 7 13s7-8 7-13a7 7 0 0 0-7-7zm0 9.5A2.5 2.5 0 1 1 12 6.5a2.5 2.5 0 0 1 0 5z"/>
    </svg>
    <div class="contact-block contact-block--address">
      <p class="contact-line">17 Corrantide Row</p>
      <p class="contact-line">London</p>
      <p class="contact-line">EC9Z 4QX</p>
      <p class="contact-line">United Kingdom</p>
    </div>

    <svg class="contact-icon" style="top:216px" viewBox="0 0 24 24" aria-hidden="true">
      <path fill="var(--accent)" d="M2 8c0-2 3-4 10-4s10 2 10 4v2h-5V8.5c-1.5-.6-3-.8-5-.8s-3.5.2-5 .8V10H2z"/>
      <path fill="var(--accent)" d="M6 11h12l2 9H4z"/>
      <g fill="#fff"><rect x="9" y="13" width="2" height="1.6"/><rect x="13" y="13" width="2" height="1.6"/><rect x="9" y="16" width="2" height="1.6"/><rect x="13" y="16" width="2" height="1.6"/></g>
    </svg>
    <div class="contact-block contact-block--phones">
      <p class="contact-line">+44 7000 481236</p>
      <p class="contact-line">+971 50 0736419</p>
      <p class="contact-line">+38 060 555 0193</p>
      <p class="contact-line">info@bramblewickkeystone.com</p>
      <p class="contact-line">www.bramblewickkeystone.com</p>
    </div>

    <svg class="contact-icon" style="top:297px" viewBox="0 0 24 24" aria-hidden="true">
      <rect x="2" y="5" width="20" height="14" fill="none" stroke="var(--accent)" stroke-width="2"/>
      <path d="M2 5l10 8 10-8M2 19l8-7M22 19l-8-7" fill="none" stroke="var(--accent)" stroke-width="1.6"/>
    </svg>
    <svg class="contact-icon" style="top:324px" viewBox="0 0 24 24" aria-hidden="true">
      <g fill="none" stroke="var(--accent)" stroke-width="1.5">
        <circle cx="12" cy="12" r="9.5" fill="var(--accent)" fill-opacity="0.25"/>
        <ellipse cx="12" cy="12" rx="4.5" ry="9.5"/>
        <path d="M2.5 12h19M4 7h16M4 17h16M12 2.5v19"/>
      </g>
    </svg>

    <div class="back-brand">
      <span class="back-brand__name">Bramblewick Keystone</span>
      <span class="back-brand__dot"></span>
    </div>
  </section>

</main>
</body>
</html>
```